Need a Wordpress website for my HVAC company

I need a Wordpress website created for an HVAC company in a competitive market.
Following are some websites I like:
My current website is www.brovikclimate.com - we also have a facebook page with some pictures

We are an airconditioning and heating company that does both residential and commmercial work.
We need the following info on our website:
-mobile friendly
-Schedule an appt -repair/maintnenace/installation (i would like this option to always be on the page even if they scroll down.)
-24 hour service
-coupons /promotions
-financing
-reviews/testimonials
-about
-blog
-Our service area
The following are services we provide:
-Air conditioning - Installation/Service/Maintenance/new construction
-Heating - Installation/Service/Maintenance/new construction ( gas furnace, 2 stage furnace, electric heat)
-Duct - Repair/Replacement/Istallation - (zone systems)
-thermostats (wifi)
-Heat pump
-Air handler
-self communicating systems
-carbon monoxide testing
-hail damage
-duct sealing
-insulation
-Air cleaners - UV Air purifiers
-humidifiers

I would also like Yoast SEO add on

Target Market(s)

Anyone who needs our services HVAC contractor

Industry/Entity Type

Hvac

Contact Information for Business Card

Phone:480-555-2946
website:www.brovikclimate.com
email pmarsh@brovikclimate.com

Coding

Coded - Design and coding required

Number of Pages Required

5+ page

Font styles to use
Serif
Sans Serif

Requirements
Must have
• I wrote in brief. I already have Webb Otter. Long story I paid for 3 years already. I need someone to put website there. Ive never used Wordpress but would like a template page so I can easily add services.
Nice to have
• Clean, bright, original

```html
<!DOCTYPE html>
<html lang="en">
<head>
<meta charset="utf-8">
<title>Brovik Climate Services — Heating &amp; Cooling</title>
<link href="https://fonts.googleapis.com/css2?family=Raleway:wght@400;500;600;700&family=Open+Sans:wght@400;600;700&display=swap" rel="stylesheet">
<style>
:root{
  --red:#c41f2c;
  --red-dark:#a9141f;
  --blue:#1c57a5;
  --blue-deep:#164a8f;
  --ink:#222428;
  --text:#3b3d42;
  --muted:#6c6f75;
  --line:#d9dbe0;
  --paper:#ffffff;
  --soft:#f1f1f1;
  --foot:#efefef;
}
*{box-sizing:border-box;margin:0;padding:0}
html,body{width:1200px;height:2894px;overflow:hidden}
body{position:relative;background:var(--paper);font-family:"Open Sans",Arial,sans-serif;color:var(--text);font-size:11px;line-height:1.7}
h1,h2,h3,h4{font-family:"Raleway","Helvetica Neue",Arial,sans-serif}

/* header */
.site-header{position:absolute;left:0;top:0;width:1200px;height:158px;background:#f7f6f4;border-bottom:3px solid var(--blue)}
.btn-schedule{position:absolute;left:162px;top:35px;width:186px;height:36px;border:1px solid #bfc1c5;border-radius:18px;font:700 11px/34px "Raleway",sans-serif;color:var(--muted);text-align:center;letter-spacing:.3px}
.nav{position:absolute;top:94px;display:flex;gap:30px;font:700 11.5px "Raleway",sans-serif;color:var(--ink);letter-spacing:.2px}
.nav .active{color:var(--red)}
.nav-left{left:162px}
.nav-right{left:796px}
.brand{position:absolute;left:520px;top:48px;width:200px;height:60px;display:flex;align-items:center;justify-content:center;gap:8px;font:700 19px "Raleway",sans-serif;color:var(--blue);letter-spacing:.5px}
.brand .dot{width:14px;height:14px;border-radius:50%;background:var(--red)}
.top-phone{position:absolute;left:772px;top:40px;font:600 20px "Raleway",sans-serif;color:var(--red);display:flex;align-items:center;gap:8px}
.social{position:absolute;left:957px;top:40px;display:flex;gap:8px}
.social span{width:26px;height:26px;border-radius:50%;border:1px solid #b9c4d6;background:#fff}

/* hero */
.hero{position:absolute;left:0;top:161px;width:1200px;height:495px;background:#fbfbfb}
.hero-kicker{position:absolute;left:162px;top:138px;font:500 21px "Raleway",sans-serif;color:var(--ink)}
.hero-title{position:absolute;left:162px;top:170px;font:700 22px "Raleway",sans-serif;color:var(--ink);letter-spacing:.6px}
.hero-copy{position:absolute;left:162px;top:214px;width:370px;font-size:11px;color:var(--text)}
.hero-call{position:absolute;left:162px;top:262px;font:600 24px "Raleway",sans-serif;color:var(--red);letter-spacing:.4px}
.slider-dots{position:absolute;display:flex;gap:5px}
.slider-dots i{display:block;width:14px;height:14px;border-radius:50%;background:#a8a8a8}
.slider-dots i.on{background:var(--red)}
.hero-art{position:absolute;left:579px;top:52px;width:463px;height:396px;border-radius:6px;background:linear-gradient(135deg,#e8edf5 0%,#c9d6ea 45%,#e9c8cb 100%)}

/* service band */
.band{position:absolute;left:0;top:656px;width:1200px;height:131px;background:var(--red)}
.band .mid{position:absolute;left:453px;top:0;width:290px;height:131px;background:var(--red-dark)}
.band-item{position:absolute;top:-62px;width:240px;text-align:center}
.band-icon{width:120px;height:120px;margin:0 auto;border-radius:50%;background:var(--red);border:4px solid #fff;display:flex;align-items:center;justify-content:center}
.band-label{margin-top:14px;font:500 22px "Raleway",sans-serif;color:#fff}

/* welcome */
.welcome h2,.reviews h2{font:500 28px "Raleway",sans-serif;color:var(--ink)}
.welcome{position:absolute;left:162px;top:846px;width:468px}
.welcome p{margin-top:14px;font-size:11px;line-height:1.75}
.video{margin-top:18px;width:468px;height:240px;position:relative;background:linear-gradient(120deg,#7a8a5c 0%,#c9c5bd 50%,#4c5360 100%)}
.play{position:absolute;left:212px;top:98px;width:44px;height:44px;border-radius:50%;background:var(--red);border:3px solid #fff}
.play:after{content:"";position:absolute;left:15px;top:10px;border-left:14px solid #fff;border-top:9px solid transparent;border-bottom:9px solid transparent}
.reviews{position:absolute;left:679px;top:846px;width:412px}
.quote{margin-top:22px;font-style:italic;font-size:10.5px;line-height:1.75;color:var(--text)}
.quote-name{margin-top:12px;font:700 10px "Open Sans",sans-serif;color:var(--blue)}
.quote-name span{color:var(--muted);font-weight:600}
.quote-mark{position:relative;margin-top:10px;height:20px;border-bottom:1px solid var(--line)}
.quote-mark b{position:absolute;left:188px;top:-4px;background:#fff;padding:0 8px;font:700 34px/34px Georgia,serif;color:var(--blue)}

/* services */
.services{position:absolute;left:0;top:1293px;width:1200px;height:469px;background:var(--blue);color:#fff;text-align:center}
.services h2{position:absolute;left:0;top:48px;width:1200px;font:600 28px "Raleway",sans-serif}
.services .intro{position:absolute;left:200px;top:104px;width:800px;font-size:10.5px;line-height:2}
.svc{position:absolute;top:184px;width:170px}
.svc .ring{width:82px;height:82px;margin:0 auto;border:2px solid #fff;border-radius:50%;display:flex;align-items:center;justify-content:center}
.svc h4{margin-top:18px;font:500 15px "Raleway",sans-serif}
.svc p{margin:8px auto 0;width:150px;font-size:10px;line-height:1.7}
.tech-left{position:absolute;left:0;top:250px;width:120px;height:219px;border-radius:4px;background:linear-gradient(180deg,#3f7fd0 0%,#2a3a5c 100%)}
.services .slider-dots i{background:#14386b}
.services .slider-dots i.on{background:#fff}

/* financing */
.perks{position:absolute;left:0;top:1762px;width:1200px;height:428px;background:var(--soft)}
.perks h2{font:700 26px "Raleway",sans-serif;color:var(--red)}
.perks p{margin-top:16px;font-size:10.5px;line-height:1.75;text-align:justify}
.perks ul{list-style:none;margin-top:14px}
.perks li{position:relative;padding-left:18px;font-size:10.5px;line-height:2}
.perks li:before{content:"";position:absolute;left:0;top:6px;width:9px;height:9px;border-radius:50%;background:var(--red)}
.perks li:after{content:"";position:absolute;left:2px;top:9px;width:3px;height:3px;border-right:1.5px solid #fff;border-top:1.5px solid #fff;transform:rotate(45deg)}
.finance{position:absolute;left:162px;top:92px;width:440px}
.why{position:absolute;left:635px;top:92px;width:300px}
.btn-more{display:inline-block;margin-top:16px;width:106px;height:36px;border:1px solid #555;border-radius:18px;font:700 9.5px/34px "Raleway",sans-serif;color:var(--ink);text-align:center}
.tech-right{position:absolute;left:952px;top:43px;width:215px;height:333px;border-radius:4px;background:linear-gradient(180deg,#6b3f22 0%,#2a66b8 35%,#26345a 100%)}

/* blog */
.blog h2{position:absolute;left:0;top:2234px;width:1200px;text-align:center;font:500 27px "Raleway",sans-serif;color:var(--ink)}
.post{position:absolute;top:2292px;width:275px}
.post .thumb{height:154px}
.post h3{margin-top:26px;font:500 17px "Raleway",sans-serif;color:var(--ink)}
.post p{margin-top:6px;font-size:10px;line-height:1.7}
.post .meta{margin-top:8px;font-size:10px;color:var(--red);display:flex;gap:16px}

/* footer */
.site-footer{position:absolute;left:0;top:2614px;width:1200px;height:280px;background:var(--foot)}
.foot-brand{position:absolute;left:162px;top:62px;display:flex;align-items:center;gap:8px;font:700 17px "Raleway",sans-serif;color:var(--blue)}
.foot-brand .dot{width:12px;height:12px;border-radius:50%;background:var(--red)}
.copy{position:absolute;left:162px;top:154px;font-size:10px;line-height:1.8;color:var(--ink)}
.pay{position:absolute;left:162px;top:220px;display:flex;gap:6px}
.pay span{width:28px;height:18px;border-radius:2px;background:#cfd3da}
.foot-col{position:absolute;top:56px}
.foot-col h4{font:500 14px "Raleway",sans-serif;color:var(--ink)}
.foot-col ul{list-style:none;margin-top:8px}
.foot-col li{font-size:10px;line-height:21px;color:var(--text)}
.tech-foot{position:absolute;left:930px;top:19px;width:115px;height:222px;border-radius:4px;background:linear-gradient(180deg,#6b3f22 0%,#2a66b8 35%,#26345a 100%)}
.live-chat{position:absolute;left:1158px;top:2739px;width:42px;height:107px;background:var(--red);color:#fff;font:700 11px "Raleway",sans-serif;letter-spacing:.6px;writing-mode:vertical-rl;transform:rotate(180deg);display:flex;align-items:center;justify-content:center;border-radius:0 4px 4px 0}
</style>
</head>
<body>

<header class="site-header">
  <div class="btn-schedule">SCHEDULE AN APPOINTMENT</div>
  <nav class="nav nav-left"><span class="active">HOME</span><span>ABOUT US</span><span>24 HOUR SERVICES</span><span>COUPONS</span></nav>
  <div class="brand"><span class="dot"></span>BROVIK CLIMATE</div>
  <div class="top-phone">
    <svg width="16" height="16" viewBox="0 0 24 24"><path fill="#c41f2c" d="M6.6 10.8a15 15 0 0 0 6.6 6.6l2.2-2.2c.3-.3.7-.4 1-.2 1.1.4 2.3.6 3.6.6.6 0 1 .4 1 1V20c0 .6-.4 1-1 1A17 17 0 0 1 3 4c0-.6.4-1 1-1h3.5c.6 0 1 .4 1 1 0 1.3.2 2.5.6 3.6.1.3 0 .7-.2 1z"/></svg>
    (480) 555-2946
  </div>
  <div class="social"><span></span><span></span><span></span></div>
  <nav class="nav nav-right"><span>FINANCING</span><span>REVIEWS</span><span>BLOG</span><span>CONTACT US</span></nav>
</header>

<section class="hero">
  <div class="hero-kicker">Your satisfaction is guaranteed</div>
  <h1 class="hero-title">OUR REPUTATION DEPENDS ON IT</h1>
  <p class="hero-copy">Lorem ipsum dolor sit amet, consectetur adipiscing elit, sed do eiusmod tempor incididunt ut labore et dolore magna al</p>
  <div class="hero-call">CALL US: (480) 555-2946</div>
  <div class="slider-dots" style="left:166px;top:361px"><i class="on"></i><i></i><i></i><i></i></div>
  <div class="hero-art" role="img" aria-label="Illustrated technician in blue uniform giving a thumbs up beside a branded service van"></div>
</section>

<section class="band">
  <div class="mid"></div>
  <div class="band-item" style="left:171px">
    <div class="band-icon"><svg width="56" height="56" viewBox="0 0 24 24" fill="none" stroke="#fff" stroke-width="2" stroke-linecap="round"><path d="M14.7 6.3a4 4 0 0 0 5 5L12 19a2.1 2.1 0 0 1-3-3z"/><path d="M5 5l4 4"/><path d="M3 7l4-4"/></svg></div>
    <div class="band-label">Repair</div>
  </div>
  <div class="band-item" style="left:480px">
    <div class="band-icon"><svg width="56" height="56" viewBox="0 0 24 24" fill="none" stroke="#fff" stroke-width="2"><circle cx="12" cy="12" r="3"/><path d="M12 2v3M12 19v3M2 12h3M19 12h3M4.9 4.9l2.1 2.1M17 17l2.1 2.1M4.9 19.1L7 17M17 7l2.1-2.1"/></svg></div>
    <div class="band-label">Maintenance</div>
  </div>
  <div class="band-item" style="left:789px">
    <div class="band-icon"><svg width="56" height="56" viewBox="0 0 24 24" fill="none" stroke="#fff" stroke-width="2" stroke-linecap="round"><circle cx="12" cy="12" r="9"/><path d="M12 7v5l3 2"/></svg></div>
    <div class="band-label">Installation</div>
  </div>
</section>

<section class="welcome">
  <h2>Welcome to Brovik Climate</h2>
  <p>Lorem ipsum dolor sit amet, consectetur adipiscing elit, sed do eiusmod tempor incididunt ut labore et dolore magna aliqua enim ad minim veniam, quis nostrud exercitation ullamco labo ris nisi ut aliquip ex ea commodo consequat. Duis aute irure dolor in reprehenderit in voluptate orem ipsum dolor sit amet, consectetur adipiscing elit, sed do eiusmod tempo.</p>
  <div class="video" role="img" aria-label="Video still of a technician servicing an outdoor air conditioning unit">
    <span class="play"></span>
  </div>
</section>

<section class="reviews">
  <h2>Our Customers Say</h2>
  <p class="quote">" Sed ut perspiciatis unde omnis iste natus error sit voluptatem accusantium doloremque laudantium, totam rem aperiam, eaque ipsa quae ab illo inventore veritatis et quasi architecto beatae vitae dicta sunt explicabo. Nemo enim ipsam voluptatem quia voluptas sit aspernatur aut odit aut fugit, sed quia consequuntur magni dolores eos qui ratione voluptatem sequi nesciunt. Neque porro quisquam est, qui dolorem ipsum "</p>
  <div class="quote-name">DARA HOLM, <span>CITY NAME</span></div>
  <div class="quote-mark"><b>“</b></div>
  <p class="quote">" Sed ut perspiciatis unde omnis iste natus error sit voluptatem accusantium doloremque laudantium, totam rem aperiam, eaque ipsa quae ab illo inventore veritatis et quasi architecto beatae vitae dicta sunt explicabo. Nemo enim ipsam voluptatem quia voluptas sit aspernatur aut odit aut fugit, sed quia consequuntur magni dolores eos qui ratione voluptatem sequi nesciunt. Neque porro quisquam est, qui dolorem ipsum "</p>
  <div class="quote-name">DARA HOLM, <span>CITY NAME</span></div>
  <div class="quote-mark"><b>“</b></div>
</section>

<section class="services">
  <h2>Our Services</h2>
  <p class="intro">Lorem ipsum dolor sit amet, consectetur adipiscing elit, sed do eiusmod tempo incididunt ut labore et dolore magna aliquat enim ad minim veniam, quis nostrud exercitation ullamco labo ris nisi ut aliquip ex ea commodo consequat.Lorem ipsum dolor sit amet, consectetur adipiscing elit, sed do eiusmod tem</p>

  <div class="svc" style="left:152px">
    <div class="ring"><svg width="40" height="40" viewBox="0 0 24 24" fill="none" stroke="#fff" stroke-width="1.6"><rect x="3" y="6" width="18" height="7" rx="1"/><path d="M7 16v3M10 16v3M14 16v3M17 16v3"/></svg></div>
    <h4>Air Conditioning</h4>
    <p>Cras mattis consectetur pursit amet fermentuleo risusrta .</p>
  </div>
  <div class="svc" style="left:334px">
    <div class="ring"><svg width="40" height="40" viewBox="0 0 24 24" fill="none" stroke="#fff" stroke-width="1.6"><path d="M3 11l9-7 9 7M5 10v10h14V10"/><path d="M12 18c-2 0-2.5-2-1-4 .5 1 1.5 1 1.5 0 1.5 1.5 1.5 4-.5 4z"/></svg></div>
    <h4>Heating</h4>
    <p>Cras mattis consectetur pursit amet fermentuleo risusrta .</p>
  </div>
  <div class="svc" style="left:515px">
    <div class="ring"><svg width="40" height="40" viewBox="0 0 24 24" fill="none" stroke="#fff" stroke-width="1.6"><path d="M10 14V5a2 2 0 0 1 4 0v9a4 4 0 1 1-4 0z"/><path d="M12 9v7"/></svg></div>
    <h4>Thermostats</h4>
    <p>Cras mattis consectetur pursit amet fermentuleo risusrta .</p>
  </div>
  <div class="svc" style="left:697px">
    <div class="ring"><svg width="40" height="40" viewBox="0 0 24 24" fill="#fff"><circle cx="12" cy="12" r="2"/><path d="M12 10c-1-4 0-7 3-7 2 0 2 4-3 7zM14 12c4-1 7 0 7 3 0 2-4 2-7-3zM12 14c1 4 0 7-3 7-2 0-2-4 3-7zM10 12c-4 1-7 0-7-3 0-2 4-2 7 3z"/></svg></div>
    <h4>Air Handler</h4>
    <p>Cras mattis consectetur pursit amet fermentuleo risusrta .</p>
  </div>
  <div class="svc" style="left:880px">
    <div class="ring"><svg width="40" height="40" viewBox="0 0 24 24" fill="none" stroke="#fff" stroke-width="1.8"><circle cx="12" cy="12" r="8"/><path d="M9 15c0-4 2-6 6-6-1 3-2 5-6 6z" fill="#fff"/></svg></div>
    <h4>Heat Pump</h4>
    <p>Cras mattis consectetur pursit amet fermentuleo risusrta .</p>
  </div>

  <div class="slider-dots" style="left:574px;top:398px"><i class="on"></i><i></i><i></i><i></i></div>
  <div class="tech-left" role="img" aria-label="Illustrated technician holding a thermometer and giving a thumbs up"></div>
</section>

<section class="perks">
  <div class="finance">
    <h2>Need Financing?</h2>
    <p>Lorem ipsum dolor sit amet, consectetur adipiscing elit, sed do eiusmod tempo incididunt ut labore et dolore magna aliquat enim ad minim veniam, quis nostrud exercitation ullamco labo ris nisi ut aliquip ex ea commodo consequat.</p>
    <ul>
      <li>Low cost same as cash financing for qualifying customers.</li>
      <li>Fast and easy application.</li>
      <li>Fast credit decisions.</li>
      <li>Monthly payments as low as $56.90 per month.</li>
      <li>No lien on your home</li>
    </ul>
    <span class="btn-more">READ MORE ➜</span>
  </div>
  <div class="why">
    <h2>Why Choose Us</h2>
    <p>Lorem ipsum dolor sit amet, consectetur adipiscing elit, sed do eiusmod tempo incididunt ut labore et dolore magna aliquat enim ad minim veniam, quis nostrud exercitation</p>
    <ul>
      <li>24/7 Emergency Service</li>
      <li>Same Day Service</li>
      <li>Highly Trained Technicians</li>
      <li>Free Energy Survey</li>
      <li>Pay by the Job, Not by the Hour</li>
      <li>Fairness and Honesty</li>
    </ul>
  </div>
  <div class="tech-right" role="img" aria-label="Illustrated technician with thermometer and wrench giving a thumbs up"></div>
</section>

<section class="blog">
  <h2>Latest from the Blog</h2>
  <article class="post" style="left:162px">
    <div class="thumb" role="img" aria-label="Photo of two technicians working on outdoor condenser units" style="background:linear-gradient(135deg,#b9bcc0,#6f7a86 55%,#b43a3a)"></div>
    <h3>Lorem ipsum dolor sit amcon</h3>
    <p>Cras mattis consectetur purus sit amet fermentu lomr bileo risus, porta ac consectetur ac, vestibulumlor ate cenas faucibus mollis interdumatti.</p>
    <div class="meta"><span>▣ Oct 25 2016</span><span>● Comments</span></div>
  </article>
  <article class="post" style="left:463px">
    <div class="thumb" role="img" aria-label="Photo of a technician kneeling beside an air conditioning unit" style="background:linear-gradient(135deg,#d9d2c4,#8a7c6a 50%,#3f4a5c)"></div>
    <h3>Lorem ipsum dolor sit amc</h3>
    <p>Cras mattis consectetur purus sit amet fermentu lomr bileo risus, porta ac consectetur ac, vestibulumlor ate cenas faucibus mollis interdumatti.</p>
    <div class="meta"><span>▣ Oct 25 2016</span><span>● Comments</span></div>
  </article>
  <article class="post" style="left:764px">
    <div class="thumb" role="img" aria-label="Photo of two condenser units beside a stone wall on a lawn" style="background:linear-gradient(180deg,#9a9588,#5d5a52 55%,#6b8f3c)"></div>
    <h3>Lorem ipsum dolor sit amco</h3>
    <p>Cras mattis consectetur purus sit amet fermentu lomr bileo risus, porta ac consectetur ac, vestibulumlor ate cenas faucibus mollis interdumatti.</p>
    <div class="meta"><span>▣ Oct 25 2016</span><span>● Comments</span></div>
  </article>
</section>

<footer class="site-footer">
  <div class="foot-brand"><span class="dot"></span>BROVIK CLIMATE</div>
  <div class="copy">© 2016 Brovik Climate Services.<br>All Copyright reserved.</div>
  <div class="pay"><span></span><span></span><span></span><span></span><span></span></div>
  <div class="foot-col" style="left:419px">
    <h4>Let Us Help You</h4>
    <ul><li>Your Account</li><li>Your Orders</li><li>Sed ut perspiciatis nde</li><li>Wtus error sit voluptat</li><li>Saccusantiu</li><li>Gdoloremque</li></ul>
  </div>
  <div class="foot-col" style="left:608px">
    <h4>Product</h4>
    <ul><li>Sed ut perspiciatis</li><li>Qnde omnis iste n</li><li>Wtus error sit voluptat</li><li>em accusantiu</li><li>Gdoloremque</li></ul>
  </div>
  <div class="foot-col" style="left:785px">
    <h4>Company</h4>
    <ul><li>Home</li><li>About us</li><li>24 hour services</li><li>Coupons</li><li>Financing</li><li>Reviews</li><li>Blog</li><li>Contact us</li></ul>
  </div>
  <div class="tech-foot" role="img" aria-label="Illustrated technician with thermometer giving a thumbs up"></div>
</footer>

<div class="live-chat">LIVE CHAT</div>

</body>
</html>
```